VENTO SAURELLE

Project name: “Vento Saurelle” website
Objective: To create an elegant website,
intuitive and responsive to present this
what is “Vento Saurelle”
See attached specifications.

```html
<!DOCTYPE html>
<html lang="en">
<head>
<meta charset="utf-8">
<title>Vento Saurelle</title>
<link href="https://fonts.googleapis.com/css2?family=Jost:wght@500;600&family=Poppins:wght@400;500;600&display=swap" rel="stylesheet">
<style>
:root{
  --forest:#2f5234;
  --forest-deep:#284a2e;
  --sage:#b7c9bc;
  --mist:#dde8e1;
  --text:#3a4a3e;
  --muted:#5f6b63;
  --white:#ffffff;
  --rule:#cfd8d2;
}
*{margin:0;padding:0;box-sizing:border-box}
html,body{width:1200px;height:3318px;overflow:hidden}
body{position:relative;font-family:"Poppins",sans-serif;color:var(--text);background:var(--white)}
.abs{position:absolute}
.heading{font-family:"Jost",sans-serif;font-weight:600;text-transform:uppercase;letter-spacing:.5px}

/* hero */
.hero{left:0;top:0;width:1200px;height:635px;overflow:hidden}
.hero-photo{position:absolute;inset:0;background:
  radial-gradient(ellipse 420px 260px at 800px 390px,#5a3a2c 0%,rgba(90,58,44,0) 70%),
  linear-gradient(180deg,#163a22 0%,#4f6e2e 30%,#8f9a3c 55%,#7d8e35 75%,#5b7428 100%)}
.hero-shade{position:absolute;inset:0;background:linear-gradient(180deg,rgba(10,35,20,.55) 0%,rgba(10,35,20,0) 30%)}
.brand{left:150px;top:100px;width:180px;text-align:center;color:var(--white);font-family:"Jost",sans-serif;font-weight:600;font-size:17px;letter-spacing:1.5px}
.brand-dot{display:block;width:62px;height:62px;border:2px solid var(--white);border-radius:50%;margin:-82px auto 20px}
.phone{left:805px;top:64px;color:var(--white);font-weight:600;font-size:18px;display:flex;align-items:center;gap:10px}
.nav{left:424px;top:113px;display:flex;gap:0;color:var(--white);font-weight:500;font-size:17px}
.nav a{color:inherit;text-decoration:none;position:absolute;white-space:nowrap}
.hero-title{left:0;top:268px;width:1200px;text-align:center;color:var(--white);font-size:52px;line-height:60px}
.btn{display:flex;align-items:center;justify-content:center;border-radius:30px;font-weight:600;text-transform:uppercase;font-size:16px}
.btn-hero{left:493px;top:403px;width:213px;height:51px;background:var(--forest);border:2px solid var(--white);color:var(--white)}

/* welcome band */
.welcome{left:0;top:635px;width:1200px;height:533px;background:var(--sage);overflow:hidden}
.welcome h2{position:absolute;left:0;top:63px;width:1200px;text-align:center;color:var(--forest);font-size:38px}
.card{position:absolute;top:146px;width:253px;height:295px;background:var(--white);border:2px solid #e9efea}
.card .icon{position:absolute;left:20px;top:14px;width:93px;height:93px;border-radius:50%;background:var(--forest);display:flex;align-items:center;justify-content:center}
.card h3{position:absolute;left:19px;top:127px;font-size:21px;font-weight:500;color:var(--forest)}
.card p{position:absolute;left:21px;top:165px;width:215px;font-size:14px;line-height:20px;color:var(--muted)}

/* what we do */
.frame{left:134px;top:1275px;width:155px;height:293px;border:2px solid #4e8a46;border-right:none;border-bottom:2px solid #4e8a46}
.frame::after{content:"";position:absolute;right:-2px;top:-2px;width:2px;height:24px;background:#4e8a46}
.house-photo{left:156px;top:1299px;width:377px;height:383px;background:linear-gradient(180deg,#3d5a7a 0%,#5b6f88 35%,#7a6a55 65%,#4f6a34 100%)}
.badge{left:401px;top:1566px;width:146px;height:146px;border-radius:50%;background:var(--white);box-shadow:0 8px 24px rgba(0,0,0,.18)}
.wwd-title{left:583px;top:1305px;color:var(--forest);font-size:38px;line-height:44px}
.wwd-lead{left:583px;top:1409px;width:480px;font-size:17px;line-height:22px;color:var(--text)}
.wwd-rule{left:583px;top:1472px;width:457px;height:1px;background:var(--rule)}
.wwd-sub{left:587px;top:1490px;font-size:21px;font-weight:600;color:var(--forest)}
.wwd-body{left:588px;top:1538px;width:485px;font-size:15.5px;line-height:23.2px;color:var(--text)}

/* about */
.about{left:0;top:1803px;width:1200px;height:488px;background:linear-gradient(180deg,#2f5538 0%,#3a6a3a 55%,#3f7038 100%)}
.about h2{position:absolute;left:133px;top:106px;color:var(--white);font-size:38px}
.about p{position:absolute;left:133px;top:166px;width:490px;color:var(--white);font-size:15.5px;line-height:23.2px}
.btn-read{left:133px;top:328px;width:153px;height:52px;background:var(--mist);color:var(--forest)}
.about-ring{left:730px;top:67px;width:342px;height:342px;border:6px solid rgba(210,225,214,.75);border-radius:50%;display:flex;align-items:center;justify-content:center;color:rgba(210,225,214,.85);font-family:"Jost",sans-serif;font-weight:600;font-size:30px;letter-spacing:2px}

/* cta */
.cta-land{left:0;top:2540px;width:1200px;height:374px;background:linear-gradient(180deg,#ffffff 0%,#c9d6c4 18%,#6f9a4c 45%,#4f8a30 70%,#3f7a28 100%)}
.cta-title{left:0;top:2352px;width:1200px;text-align:center;font-family:"Jost",sans-serif;font-weight:600;font-size:48px;line-height:52px;color:var(--forest)}
.cta-text{left:280px;top:2472px;width:640px;text-align:center;font-size:19.5px;line-height:23.5px;color:var(--forest)}
.btn-quote{left:511px;top:2570px;width:178px;height:51px;background:var(--forest-deep);color:var(--white)}

/* footer */
.footer{left:0;top:2914px;width:1200px;height:404px;background:#365b3a;color:var(--white)}
.f-brand{position:absolute;left:110px;top:193px;width:275px;text-align:center;font-family:"Jost",sans-serif;font-weight:600;font-size:25px;letter-spacing:2px}
.f-brand-dot{position:absolute;left:195px;top:76px;width:104px;height:104px;border:3px solid var(--white);border-radius:50%}
.f-copy{position:absolute;left:110px;top:251px;width:275px;text-align:center;font-size:15px}
.f-rule{position:absolute;top:58px;width:1px;height:304px;background:rgba(255,255,255,.35)}
.f-head{position:absolute;top:70px;font-size:30px;font-weight:500}
.f-item{position:absolute;left:508px;display:flex;align-items:center;gap:12px;font-size:15px;line-height:22px}
.f-icon{width:46px;height:46px;border:2px solid var(--white);border-radius:50%;display:flex;align-items:center;justify-content:center;flex:none}
.f-links{position:absolute;left:951px;top:148px;list-style:none;font-size:15px;line-height:32px}
</style>
</head>
<body>

<section class="abs hero">
  <div class="hero-photo" role="img" aria-label="Hand placing a small model house on a sunlit lawn"></div>
  <div class="hero-shade"></div>
  <div class="abs brand"><span class="brand-dot"></span>VENTO SAURELLE</div>
  <div class="abs phone">
    <svg width="14" height="14" viewBox="0 0 24 24" fill="#fff"><path d="M6.6 10.8a15.1 15.1 0 0 0 6.6 6.6l2.2-2.2a1 1 0 0 1 1-.25 11.4 11.4 0 0 0 3.6.57 1 1 0 0 1 1 1V20a1 1 0 0 1-1 1A17 17 0 0 1 3 4a1 1 0 0 1 1-1h3.5a1 1 0 0 1 1 1c0 1.25.2 2.45.57 3.57a1 1 0 0 1-.25 1z"/></svg>
    Call: (555)304-2187
  </div>
  <nav class="abs nav">
    <a style="left:0">Home</a>
    <a style="left:85px">What We Do</a>
    <a style="left:222px">About Us</a>
    <a style="left:332px">Location</a>
    <a style="left:438px">Contact</a>
    <a style="left:544px">FAQ</a>
  </nav>
  <h1 class="abs heading hero-title">Welcome to<br>Vento Saurelle</h1>
  <a class="abs btn btn-hero">Get Started Here</a>
</section>

<section class="abs welcome">
  <h2 class="heading">Welcome to Vento Saurelle</h2>
  <div class="card" style="left:131px">
    <div class="icon"><svg width="44" height="44" viewBox="0 0 44 44" fill="none" stroke="#fff" stroke-width="2"><circle cx="22" cy="18" r="10"/><text x="22" y="23" text-anchor="middle" fill="#fff" stroke="none" font-size="13" font-family="Poppins">$</text><path d="M4 34h10l8 4 16-6"/></svg></div>
    <h3>Loremispmusn</h3>
    <p>Lorem ipsum dolor sit amet, consectetur adipiscing elit, sed do eiusmod tempor inci didunt ut labore et dolore magna aliqua uis.</p>
  </div>
  <div class="card" style="left:403px">
    <div class="icon"><svg width="46" height="46" viewBox="0 0 46 46" fill="none" stroke="#fff" stroke-width="2"><circle cx="13" cy="12" r="4"/><path d="M6 38V24l34-6v20z M6 30c10-2 20-8 34-10"/></svg></div>
    <h3>Loremispmusn</h3>
    <p>Lorem ipsum dolor sit amet, consectetur adipiscing elit, sed do eiusmod tempor inci didunt ut labore et dolore magna aliqua uis.</p>
  </div>
  <div class="card" style="left:676px">
    <div class="icon"><svg width="46" height="46" viewBox="0 0 46 46" fill="none" stroke="#fff" stroke-width="2"><path d="M5 22 23 6l18 16 M10 18v20h26V18"/><rect x="16" y="22" width="14" height="12"/><path d="M23 22v12M16 28h14"/></svg></div>
    <h3>Loremispmusn</h3>
    <p>Lorem ipsum dolor sit amet, consectetur adipiscing elit, sed do eiusmod tempor inci didunt ut labore et dolore magna aliqua uis.</p>
  </div>
  <div class="card" style="left:949px">
    <div class="icon"><svg width="46" height="46" viewBox="0 0 46 46" fill="none" stroke="#fff" stroke-width="2"><circle cx="17" cy="30" r="10"/><text x="17" y="35" text-anchor="middle" fill="#fff" stroke="none" font-size="13" font-family="Poppins">$</text><path d="M30 26V12 M30 18c-6 0-8-6-8-8 6 0 8 4 8 8zM30 16c0-6 6-8 8-8 0 6-4 8-8 8z"/></svg></div>
    <h3>Loremispmusn</h3>
    <p>Lorem ipsum dolor sit amet, consectetur adipiscing elit, sed do eiusmod tempor inci didunt ut labore et dolore magna aliqua uis.</p>
  </div>
</section>

<div class="abs frame"></div>
<div class="abs house-photo" role="img" aria-label="Blue craftsman house with stone path at dusk"></div>
<div class="abs badge"></div>
<h2 class="abs heading wwd-title">Vento Saurelle<br>What We Are Doing</h2>
<p class="abs wwd-lead">Lorem ipsum dolor sit amet, consectetur adipiscing elit, sed do eiusmod tempor incididunt ut labore</p>
<div class="abs wwd-rule"></div>
<h3 class="abs wwd-sub">Lorem ipsum dolor sit amet, consectetur</h3>
<p class="abs wwd-body">Lorem ipsum dolor sit amet, consectetur adipiscing elit, sed do eiusmod tempor incididunt ut labore et dolore magna aliqua Quis ipsum suspendisse ultrices gravida. Risus commodo viv rra maecenas accumsan lacus vel facilisis. Lorem ipsum dolor sit amet, consectetur adipiscing elit, sed do eiusmod tempor incididunt ut labore et dolore magna aliqua.</p>

<section class="abs about">
  <h2 class="heading">About Vento Saurelle</h2>
  <p>Lorem ipsum dolor sit amet, consectetur adipiscing elit, sed do eiusmod tempor incididunt ut labore et dolore magna aliqua Quis ipsum suspendisse ultrices gravida. Risus commodo viv rra maecenas accumsan lacus vel facilisis. Lorem ipsum dolor sit amet, consectetur adipiscing elit, sed do eiusmod tempor incididunt ut labore et dolore magna aliqua.</p>
  <a class="abs btn btn-read">Read More</a>
  <div class="abs about-ring">VENTO SAURELLE</div>
</section>

<div class="abs cta-land" role="img" aria-label="Aerial view of green farmland under morning mist"></div>
<h2 class="abs cta-title">Lorem ipsum dolor sit amet<br>consectetur adipiscin</h2>
<p class="abs cta-text">Lorem ipsum dolor sit amet, consectetur adipiscing elit, sed do eiusmod tempor incididunt ut labore et dolore magna aliquauis ipsum suspendisse ultrices gravida. Risus commodo</p>
<a class="abs btn btn-quote">Get a Quote</a>

<footer class="abs footer">
  <span class="f-brand-dot"></span>
  <div class="f-brand">VENTO SAURELLE</div>
  <div class="f-copy">© 2025 All Rights are Reserved.</div>
  <div class="f-rule" style="left:438px"></div>
  <div class="f-rule" style="left:846px"></div>
  <h4 class="f-head" style="left:507px">Contact</h4>
  <div class="f-item" style="top:137px">
    <span class="f-icon"><svg width="16" height="20" viewBox="0 0 16 20" fill="#fff"><path d="M8 0a7 7 0 0 0-7 7c0 5 7 13 7 13s7-8 7-13a7 7 0 0 0-7-7zm0 9.5A2.5 2.5 0 1 1 8 4.5a2.5 2.5 0 0 1 0 5z"/></svg></span>
    <span>42 Linden Row<br>Harlow, ME 04021</span>
  </div>
  <div class="f-item" style="top:201px">
    <span class="f-icon"><svg width="18" height="18" viewBox="0 0 24 24" fill="#fff"><path d="M6.6 10.8a15.1 15.1 0 0 0 6.6 6.6l2.2-2.2a1 1 0 0 1 1-.25 11.4 11.4 0 0 0 3.6.57 1 1 0 0 1 1 1V20a1 1 0 0 1-1 1A17 17 0 0 1 3 4a1 1 0 0 1 1-1h3.5a1 1 0 0 1 1 1c0 1.25.2 2.45.57 3.57a1 1 0 0 1-.25 1z"/></svg></span>
    <span>Phone: 555-304-2187<br>Fax: 555-304-2188</span>
  </div>
  <div class="f-item" style="top:265px">
    <span class="f-icon"><svg width="18" height="14" viewBox="0 0 18 14" fill="#fff"><path d="M0 0h18v2L9 8 0 2z M0 4l9 6 9-6v10H0z"/></svg></span>
    <span>Emial:<br>HELLO@VENTOSAURELLE.COM</span>
  </div>
  <h4 class="f-head" style="left:951px">Links</h4>
  <ul class="f-links">
    <li>Home</li><li>About</li><li>What We Do</li><li>Contact</li><li>FAQ</li>
  </ul>
</footer>

</body>
</html>
```